Business Card Design Project

Looking for a cool, trendy design for new business cards for our Mobile Application business.

QuillNest Apps

www.quillnestapps.example

Target Market(s)

Looking for a bold modern design that attracts a younger demographic in the mobile space.

Industry/Entity Type

Business

Requirements
Must have
• Trendy, Easily adapted for other staff cards, works with large clients but showcases and innovative company

```html
<!DOCTYPE html>
<html lang="en">
<head>
<meta charset="utf-8">
<title>QuillNest Apps – Business Card Options</title>
<link rel="stylesheet" href="https://fonts.googleapis.com/css2?family=Oswald:wght@700&family=Roboto+Condensed:wght@400;700&family=Roboto:wght@400&display=swap">
<style>
  :root {
    --canvas: #e6e6e6;
    --card: #ffffff;
    --ink: #111111;
    --accent: #e8a317;
    --yellow-light: #ffe36a;
    --yellow: #ffc21a;
    --orange: #f49a10;
    --orange-deep: #e67e0a;
    --peach-light: #fde6c2;
    --peach: #fbd39a;
    --shadow: rgba(0,0,0,0.22);
  }
  * { box-sizing: border-box; margin: 0; padding: 0; }
  html, body { width: 1200px; height: 818px; overflow: hidden; }
  body {
    position: relative;
    background: var(--canvas);
    font-family: "Roboto Condensed", sans-serif;
    color: var(--ink);
  }
  .option-number {
    position: absolute;
    top: 64px;
    width: 40px;
    margin-left: -20px;
    text-align: center;
    font-family: "Roboto", sans-serif;
    font-size: 30px;
    color: var(--ink);
  }
  .card {
    position: absolute;
    left: var(--x);
    top: var(--y);
    width: 170px;
    height: 262px;
    background: var(--card);
    overflow: hidden;
    box-shadow: 0 6px 14px var(--shadow);
  }
  .front-artwork {
    position: absolute;
    inset: 0;
    background:
      radial-gradient(ellipse 120px 150px at 0% 100%, var(--card) 0 55%, rgba(255,255,255,0) 100%),
      linear-gradient(135deg, var(--yellow-light) 0%, var(--yellow) 40%, var(--orange) 75%, var(--orange-deep) 100%);
  }
  .back-artwork {
    position: absolute;
    left: 0; top: 0;
    width: 170px;
    height: 160px;
    background: linear-gradient(170deg, var(--peach) 0%, var(--peach-light) 55%, rgba(255,255,255,0) 100%);
  }
  .holder-name {
    position: absolute;
    font-family: "Roboto Condensed", sans-serif;
    font-size: 15px;
    line-height: 1;
    letter-spacing: -0.2px;
    white-space: nowrap;
  }
  .holder-name .holder-role {
    display: block;
    margin-top: 2px;
    font-size: 7px;
    letter-spacing: 2.6px;
  }
  .holder-name.top-left { top: 24px; left: 22px; }
  .holder-name.top-left .holder-role { padding-left: 14px; }

  /* Front */
  .brand-block {
    position: absolute;
    left: 14px;
    top: 128px;
  }
  .brand-mark {
    width: 38px;
    height: 38px;
    background: var(--ink);
    margin-left: 16px;
  }
  .wordmark {
    font-family: "Oswald", sans-serif;
    font-weight: 700;
    font-size: 13px;
    line-height: 1.1;
    letter-spacing: 0.2px;
    white-space: nowrap;
  }
  .tagline {
    font-size: 5.5px;
    line-height: 1.2;
    letter-spacing: 0.8px;
    text-transform: uppercase;
    white-space: nowrap;
  }
  .brand-block .wordmark { margin-top: 40px; }
  .front-url {
    position: absolute;
    left: 0; right: 0;
    bottom: 10px;
    text-align: center;
    font-size: 7px;
    font-weight: 700;
    letter-spacing: 0.6px;
  }

  /* Back */
  .back-mark {
    position: absolute;
    left: 58px;
    top: 50px;
    width: 54px;
    height: 54px;
    background: var(--ink);
  }
  .back-brand {
    position: absolute;
    left: 0; right: 0;
    text-align: center;
  }
  .back-brand .wordmark { font-size: 18px; }
  .back-brand .tagline { font-size: 6px; letter-spacing: 1.2px; }
  .back-name {
    position: absolute;
    left: 0; right: 0;
    text-align: center;
    font-size: 13px;
    line-height: 1;
  }
  .back-name .holder-role {
    display: block;
    margin-top: 2px;
    font-size: 7px;
    letter-spacing: 2.6px;
  }
  .back-name.highlight { color: var(--accent); }
  .back-name.highlight .holder-role { color: var(--ink); }
  .contact {
    position: absolute;
    left: 0; right: 0;
    bottom: 10px;
    text-align: center;
    font-size: 6.5px;
    font-weight: 700;
    line-height: 1.6;
    letter-spacing: 0.4px;
  }
</style>
</head>
<body>

<div class="option-number" style="left:274px">1</div>
<div class="option-number" style="left:472px">2</div>
<div class="option-number" style="left:683px">3</div>
<div class="option-number" style="left:893px">4</div>

<!-- Fronts -->
<section class="card card-front" style="--x:189px; --y:110px">
  <div class="front-artwork" role="img" aria-label="Abstract overlapping yellow and orange swoosh artwork"></div>
  <div class="brand-block">
    <div class="brand-mark"></div>
    <div class="wordmark">QuillNest Apps</div>
    <div class="tagline">Mobile software for<br>professional development</div>
  </div>
  <div class="front-url">www.quillnestapps.example</div>
</section>

<section class="card card-front" style="--x:390px; --y:110px">
  <div class="front-artwork" role="img" aria-label="Abstract overlapping yellow and orange swoosh artwork"></div>
  <div class="holder-name top-left">DALE MARSH<span class="holder-role">FOUNDER</span></div>
  <div class="brand-block">
    <div class="brand-mark"></div>
    <div class="wordmark">QuillNest Apps</div>
    <div class="tagline">Mobile software for<br>professional development</div>
  </div>
  <div class="front-url">www.quillnestapps.example</div>
</section>

<section class="card card-front" style="--x:605px; --y:110px">
  <div class="front-artwork" role="img" aria-label="Abstract overlapping yellow and orange swoosh artwork"></div>
  <div class="brand-block">
    <div class="brand-mark"></div>
    <div class="wordmark">QuillNest Apps</div>
    <div class="tagline">Mobile software for<br>professional development</div>
  </div>
  <div class="front-url">www.quillnestapps.example</div>
</section>

<section class="card card-front" style="--x:809px; --y:110px">
  <div class="front-artwork" role="img" aria-label="Abstract overlapping yellow and orange swoosh artwork"></div>
  <div class="brand-block">
    <div class="brand-mark"></div>
    <div class="wordmark">QuillNest Apps</div>
    <div class="tagline">Mobile software for<br>professional development</div>
  </div>
  <div class="front-url">www.quillnestapps.example</div>
</section>

<!-- Backs -->
<section class="card card-back" style="--x:189px; --y:433px">
  <div class="back-artwork" role="img" aria-label="Faint peach swoosh artwork"></div>
  <div class="back-mark"></div>
  <div class="back-brand" style="top:150px">
    <div class="wordmark">QuillNest Apps</div>
    <div class="tagline">Mobile software for<br>professional development</div>
  </div>
  <div class="back-name highlight" style="top:195px">DALE MARSH<span class="holder-role">FOUNDER</span></div>
  <div class="contact">Phone:1-555-700-0142<br>Email:dale@quillnestapps.example<br>www.quillnestapps.example</div>
</section>

<section class="card card-back" style="--x:390px; --y:433px">
  <div class="back-artwork" role="img" aria-label="Faint peach swoosh artwork"></div>
  <div class="back-mark"></div>
  <div class="back-brand" style="top:153px">
    <div class="wordmark">QuillNest Apps</div>
    <div class="tagline">Mobile software for<br>professional development</div>
  </div>
  <div class="contact" style="bottom:14px">Phone:1-555-700-0142<br>Email:dale@quillnestapps.example<br>www.quillnestapps.example</div>
</section>

<section class="card card-back" style="--x:605px; --y:433px">
  <div class="back-artwork" role="img" aria-label="Faint peach swoosh artwork"></div>
  <div class="back-mark"></div>
  <div class="back-brand" style="top:150px">
    <div class="wordmark">QuillNest Apps</div>
    <div class="tagline">Mobile software for<br>professional development</div>
  </div>
  <div class="back-name" style="top:194px">DALE MARSH<span class="holder-role">FOUNDER</span></div>
  <div class="contact">Phone:1-555-700-0142<br>Email:dale@quillnestapps.example<br>www.quillnestapps.example</div>
</section>

<section class="card card-back" style="--x:809px; --y:433px">
  <div class="back-artwork" role="img" aria-label="Faint peach swoosh artwork"></div>
  <div class="holder-name top-left" style="top:12px; left:12px; font-size:13px">DALE MARSH<span class="holder-role">FOUNDER</span></div>
  <div class="back-mark"></div>
  <div class="back-brand" style="top:162px">
    <div class="wordmark">QuillNest Apps</div>
    <div class="tagline">Mobile software for<br>professional development</div>
  </div>
  <div class="contact" style="bottom:14px">Phone:1-555-700-0142<br>Email:dale@quillnestapps.example<br>www.quillnestapps.example</div>
</section>

</body>
</html>
```